Lantern Motion for Neighbors Business Cards

I need business cards for staff in a new startup. Our company name is Movrela - we train Tai Chi teachers. But our biggest project is called Lantern Motion for Neighbors - a federal project to put together free Tai Chi classes for Vets all across America. It's a young company, with a spirit of excitement, passion, a desire to do good for others (our Vets) and a modern style and sensibility. In other words, not old-fashioned Asian martial arts theme, but something new.

Industry/Entity Type

Health And Wellness

Contact Information for Business Card

The topic is ancient healing, but the company is the Pembrooks - so I'd like a card design that captures that.

Font styles to use
Sans Serif

Colors

Designer to choose colors to be used in the design.

Requirements
Nice to have
• I've got two logos - one for the company and one for the project. I want to see if we can incorporate them both without it becoming too busy.
Should not have
• Overly old-fashioned yin-yang themes.

```html
<!DOCTYPE html>
<html lang="en">
<head>
<meta charset="utf-8">
<title>Lantern Motion for Neighbors — Business Card</title>
<link rel="stylesheet" href="https://fonts.googleapis.com/css2?family=Lato:wght@400;700&display=swap">
<style>
  :root {
    --backdrop: #e9e6e2;
    --card-light: #f4f3f1;
    --navy: #2e3566;
    --red: #d1252c;
    --deep-red: #5a0a10;
    --mid-red: #9c1420;
    --gold: #d9b63a;
    --ink-light: #f1e6e4;
    --ink-muted: #d9a9a9;
  }
  html, body {
    margin: 0;
    width: 1200px;
    height: 969px;
    overflow: hidden;
    background: var(--backdrop);
  }
  .business-card {
    position: absolute;
    left: 120px;
    top: 210px;
    width: 960px;
    height: 548px;
    border-radius: 24px;
    overflow: hidden;
    background: var(--card-light);
    box-shadow: 0 10px 30px rgba(0,0,0,0.18);
    font-family: "Lato", sans-serif;
  }
  .edge-decoration {
    position: absolute;
    left: 0;
    top: 0;
    width: 120px;
    height: 100%;
    background: linear-gradient(90deg, var(--navy) 0%, rgba(46,53,102,0.55) 45%, rgba(209,37,44,0.25) 75%, rgba(244,243,241,0) 100%);
  }
  .card-art {
    position: absolute;
    inset: 0;
  }
  .project-name {
    position: absolute;
    left: 100px;
    top: 80px;
    display: flex;
    align-items: center;
    gap: 16px;
  }
  .project-name .mark-dot {
    width: 46px;
    height: 46px;
    border-radius: 50%;
    background: var(--navy);
    flex: none;
  }
  .project-name span {
    color: var(--navy);
    font-weight: 700;
    font-size: 30px;
    line-height: 1.1;
    width: 300px;
  }
  .company-name {
    position: absolute;
    left: 210px;
    top: 290px;
    display: flex;
    align-items: center;
    gap: 18px;
  }
  .company-name .mark-dot {
    width: 110px;
    height: 110px;
    border-radius: 50%;
    background: var(--red);
    flex: none;
  }
  .company-name span {
    color: var(--red);
    font-weight: 700;
    font-size: 44px;
  }
  .contact-block {
    position: absolute;
    right: 50px;
    top: 112px;
    text-align: right;
    color: var(--ink-light);
  }
  .person-name {
    margin: 0;
    color: var(--gold);
    font-weight: 700;
    font-size: 30px;
    line-height: 36px;
  }
  .person-role {
    margin: 0 0 26px;
    font-size: 21px;
    line-height: 28px;
  }
  .address {
    margin: 0 0 24px;
    font-size: 21px;
    line-height: 28px;
  }
  .contact-list {
    list-style: none;
    margin: 0;
    padding: 0;
  }
  .contact-list li {
    display: flex;
    justify-content: flex-end;
    align-items: center;
    gap: 12px;
    font-size: 20px;
    line-height: 27px;
  }
  .contact-list li.online {
    color: var(--ink-muted);
    font-size: 19px;
  }
  .contact-list svg {
    width: 16px;
    height: 16px;
    fill: var(--gold);
    flex: none;
  }
</style>
</head>
<body>
  <div class="business-card">
    <div class="edge-decoration" role="img" aria-label="Decorative flowing swoosh in navy and red along the left edge"></div>

    <svg class="card-art" viewBox="0 0 960 548" preserveAspectRatio="none" aria-hidden="true">
      <defs>
        <radialGradient id="panel-glow" cx="0.45" cy="0.3" r="0.8">
          <stop offset="0" stop-color="#9c1420"/>
          <stop offset="0.6" stop-color="#6e0c15"/>
          <stop offset="1" stop-color="#5a0a10"/>
        </radialGradient>
      </defs>
      <path d="M520 0 C600 120 610 260 570 380 C545 450 510 510 500 548 L960 548 L960 0 Z" fill="url(#panel-glow)"/>
      <path d="M520 0 C600 120 610 260 570 380 C545 450 510 510 500 548" fill="none" stroke="#d9b63a" stroke-width="7"/>
    </svg>

    <div class="project-name">
      <div class="mark-dot"></div>
      <span>Lantern Motion for Neighbors</span>
    </div>

    <div class="company-name">
      <div class="mark-dot"></div>
      <span>Movrela</span>
    </div>

    <div class="contact-block">
      <p class="person-name">Daniel Harrow</p>
      <p class="person-role">President</p>
      <p class="address">2140 Cedar Ridge Road<br>Fairbanks, Alaska 34812</p>
      <ul class="contact-list">
        <li>555-214-8630
          <svg viewBox="0 0 16 16"><path d="M3 1l3 0 1 4-2 1c1 2 3 4 5 5l1-2 4 1 0 3c0 1-1 2-2 2C7 15 1 9 1 3c0-1 1-2 2-2z"/></svg>
        </li>
        <li>555-390-2174
          <svg viewBox="0 0 16 16"><path d="M4 0h8a1 1 0 0 1 1 1v14a1 1 0 0 1-1 1H4a1 1 0 0 1-1-1V1a1 1 0 0 1 1-1zm1 2v10h6V2zm3 11a1 1 0 1 0 0 2 1 1 0 0 0 0-2z"/></svg>
        </li>
        <li>555-471-6025
          <svg viewBox="0 0 16 16"><path d="M4 1h8v4H4zM1 6h14v6h-2v3H3v-3H1zm4 4v3h6v-3z"/></svg>
        </li>
        <li class="online">info@lanternmotion.org
          <svg viewBox="0 0 16 16"><path d="M1 3h14v10H1zm1 1v1l6 4 6-4V4z"/></svg>
        </li>
        <li class="online">www.lanternmotion.org
          <svg viewBox="0 0 16 16"><path d="M8 1a7 7 0 1 0 0 14A7 7 0 0 0 8 1zm-1 2 2 2-1 2 3 1v3l-2 2V9L5 8 4 5z"/></svg>
        </li>
      </ul>
    </div>
  </div>
</body>
</html>
```